Rejuvenate Canada Natural SkinCare Brand packaging box

Tessa Brandt Natural Producat based in Canada B.C.Miss Tessa Brandt is the founder of the company, she is a reflexologist therapist. The hero product are Tessa Brandt Velvet Salve and Massage oil, the product help her clients to allievate many skin problems and sore msucle condition.

The formula of Tessa Brandt Natural Product is based on a recipe that was used by many generations of a Belgium family.The recipe survived the "Chemicalization" of natural remedies as it is believed that pure, natural remedies have superior healing abilities. The recipes used three main herbs: St. John's wort, Calendula and arnica.

We would like to see designs that use our classical green color (brand color) and the three flowers components (St. John's wort, Calendula and arnica) to rejuvenate the packaging. Since we will keep adding new product to the line. We want to see a contemporary, simple and natural design, so that the customer able to recognize our brand and outstanding the product on the shelf.

The Tessa Brandt logo remains or could simply. The 3 flowers could present or use simple graphic or outline.

For details of existing design, please refer www.tessabrandt-example.com.hk

Target Market(s)

For 40-70 women market

Industry/Entity Type

It Company

Font styles to use
Serif

Requirements
Must have
• Tessa Brandt Logo
• Brand green color (RBG R:56 G:152 B:3)
• 3 main flowers ingredients ( in simple graphic/ outline)
• outstanding on the shelf
• Natural, simple and contemporary
• Strong branding
• Not too colorful
• Easily identify different product in the same brand
• (Velvet Salve, Massage oil, face oil, healing balm stick, pain ointment)
Nice to have
• Hot-stamping silver or embossed pattern is optional
• ecologo, no animal test, 100% all natural, vegan, non GMO, paraben free
Should not have
• Too fancy approach

```html
<!DOCTYPE html>
<html lang="en">
<head>
<meta charset="utf-8">
<title>Tessa Brandt – Rejuvenate Label Set</title>
<link rel="stylesheet" href="https://fonts.googleapis.com/css2?family=Roboto:wght@300;400&display=swap">
<style>
  :root {
    --page: #ffffff;
    --label-top: #f1f2f2;
    --label-top-edge: #e3e4e4;
    --brand-brown: #8b3b2b;
    --brand-dot: #f5c518;
    --title-grey: #555759;
    --band-dark: #3f4040;
    --band-text: #f2f2f2;
    --green-deep: #79bf2a;
    --green-light: #d9ef8f;
    --green-text: #4f5a3a;
    --leaf-red: #d7261e;
    --bloom-purple: #b3368f;
    --bloom-white: #f6f3ee;
    --bloom-leaf: #9cc46a;
  }
  * { box-sizing: border-box; margin: 0; padding: 0; }
  html, body {
    width: 1200px; height: 1200px; overflow: hidden;
    background: var(--page);
    font-family: "Roboto", Arial, sans-serif;
  }
  .label-set {
    width: 1200px; height: 1200px;
    display: flex; justify-content: center; align-items: center; gap: 80px;
  }
  .label {
    width: 440px; height: 980px;
    display: flex; flex-direction: column;
    border-radius: 18px; overflow: hidden;
    box-shadow: 0 0 0 1px var(--label-top-edge);
  }
  .label__top {
    flex: 1 1 auto;
    background: linear-gradient(180deg, #ffffff 0%, var(--label-top) 100%);
    display: flex; flex-direction: column; align-items: center;
    padding-top: 70px;
  }
  .brand {
    display: flex; align-items: center; gap: 12px;
    color: var(--brand-brown);
    font-weight: 400; font-size: 46px; letter-spacing: 0.5px;
  }
  .brand__dot {
    width: 20px; height: 20px; border-radius: 50%;
    background: var(--brand-dot);
  }
  .product-name {
    margin-top: 48px;
    color: var(--title-grey);
    font-weight: 300; font-size: 42px; line-height: 1.12;
    text-align: center;
  }
  .floral {
    margin-top: 34px;
    width: 340px; height: 300px;
    border-radius: 50%;
    background:
      radial-gradient(circle at 55% 62%, var(--bloom-purple) 0 22%, transparent 40%),
      radial-gradient(circle at 28% 55%, var(--bloom-white) 0 20%, transparent 34%),
      radial-gradient(circle at 72% 28%, var(--bloom-leaf) 0 10%, transparent 26%),
      radial-gradient(circle at 50% 35%, #ffffff 0 18%, transparent 36%);
  }
  .band-formula {
    background: var(--band-dark);
    color: var(--band-text);
    text-align: center;
    font-weight: 300; font-size: 30px; line-height: 1.25;
    padding: 16px 10px;
  }
  .band-origin {
    height: 300px;
    background: linear-gradient(180deg, var(--green-deep) 0%, var(--green-light) 100%);
    display: flex; flex-direction: column; align-items: center;
    padding-top: 26px;
    color: var(--green-text);
  }
  .origin__claim { font-weight: 300; font-size: 19px; }
  .origin__since { font-weight: 400; font-size: 19px; margin-top: 6px; }
  .origin__leaf {
    margin-top: 34px;
    width: 84px; height: 84px; border-radius: 50%;
    background: var(--leaf-red);
  }
  .origin__made { margin-top: 26px; font-weight: 300; font-size: 19px; }
</style>
</head>
<body>
  <main class="label-set">
    <section class="label">
      <div class="label__top">
        <div class="brand"><span class="brand__dot"></span>Tessa Brandt</div>
        <h2 class="product-name">Aromatic<br>Moisturiser</h2>
        <div class="floral" role="img" aria-label="Illustration of a purple peony with white jasmine blossoms and green leaves"></div>
      </div>
      <div class="band-formula">Rejuvenate<br>Anti-Winkle Formula</div>
      <div class="band-origin">
        <p class="origin__claim">100% Natural Herbal Ingredients</p>
        <p class="origin__since">Since 1995</p>
        <div class="origin__leaf" role="img" aria-label="Red maple leaf symbol"></div>
        <p class="origin__made">Made in canada</p>
      </div>
    </section>

    <section class="label">
      <div class="label__top">
        <div class="brand"><span class="brand__dot"></span>Tessa Brandt</div>
        <h2 class="product-name">Face Cream</h2>
        <div class="floral" role="img" aria-label="Illustration of a purple peony with white jasmine blossoms and green leaves"></div>
      </div>
      <div class="band-formula">Rejuvenate<br>Anti-Winkle Formula</div>
      <div class="band-origin">
        <p class="origin__claim">100% Natural Herbal Ingredients</p>
        <p class="origin__since">Since 1995</p>
        <div class="origin__leaf" role="img" aria-label="Red maple leaf symbol"></div>
        <p class="origin__made">Made in canada</p>
      </div>
    </section>
  </main>
</body>
</html>
```